Updated Buisness card/Design

Target Market(s)

Residential clients

Industry/Entity Type

Interior remodeling

Contact Information for Business Card

see mark up

Requirements
Must have
• Logo

```html
<!DOCTYPE html>
<html lang="en">
<head>
<meta charset="utf-8">
<title>Hillcrest Building Group – Business Card</title>
<link href="https://fonts.googleapis.com/css2?family=Open+Sans:wght@400;600;700&family=Montserrat:wght@700&display=swap" rel="stylesheet">
<style>
  :root {
    --stage: #232323;
    --brand-blue: #3a9ad9;
    --brand-blue-pale: #e6eef9;
    --ink: #1d1d1f;
    --grey-light: #9aa0a8;
    --grey-mid: #858b94;
    --grey-dark: #6f747c;
    --white: #ffffff;
  }
  * { box-sizing: border-box; margin: 0; padding: 0; }
  html, body {
    width: 1200px; height: 780px; overflow: hidden;
    background: var(--stage);
    font-family: "Open Sans", Arial, sans-serif;
  }
  .stage {
    position: relative; width: 1200px; height: 780px;
    display: flex; align-items: center; justify-content: center; gap: 40px;
  }
  .card {
    position: relative; width: 540px; height: 310px;
    border-radius: 22px; overflow: hidden;
    border-bottom: 4px solid var(--brand-blue);
    box-shadow: 0 14px 30px rgba(0,0,0,.55);
  }

  /* Back side */
  .card-back { background: linear-gradient(160deg, var(--grey-light), var(--grey-mid) 55%, var(--grey-dark)); }
  .card-back .pattern {
    position: absolute; inset: 0;
    background: linear-gradient(150deg, rgba(255,255,255,.18), rgba(0,0,0,.12));
  }
  .card-back .brand {
    position: absolute; left: 28px; top: 28px;
    display: flex; align-items: center; gap: 8px;
    color: var(--white); font-weight: 700; font-size: 14px; letter-spacing: .04em;
    text-transform: uppercase;
  }
  .brand-square { width: 12px; height: 12px; background: currentColor; flex: none; }
  .services {
    position: absolute; left: 28px; right: 28px; bottom: 30px;
    color: var(--white); font-size: 13px; line-height: 1.55; text-align: right;
  }
  .services .dot {
    display: inline-block; width: 7px; height: 7px; border-radius: 50%;
    background: var(--brand-blue); margin: 0 6px 1px;
  }

  /* Front side */
  .card-front { background: var(--white); }
  .card-front .brand {
    position: absolute; left: 30px; top: 36px;
    display: flex; align-items: center; gap: 9px;
    color: var(--brand-blue); font-weight: 700; font-size: 17px; letter-spacing: .03em;
    text-transform: uppercase;
  }
  .holder {
    position: absolute; right: 0; top: 100px; text-align: right;
    display: flex; align-items: flex-start; gap: 10px;
  }
  .holder-name {
    font-family: "Montserrat", "Open Sans", sans-serif; font-weight: 700;
    font-size: 32px; line-height: 1; color: var(--brand-blue);
  }
  .holder-name .surname { color: var(--grey-dark); }
  .holder-title { font-size: 12px; color: var(--ink); margin-top: 6px; }
  .holder-bar { width: 14px; height: 34px; background: var(--brand-blue); }
  .address {
    position: absolute; left: 30px; top: 112px;
    font-size: 14px; line-height: 1.4; color: var(--ink);
  }
  .contacts {
    position: absolute; left: 30px; bottom: 26px; list-style: none;
    font-size: 14px; line-height: 1.5; color: var(--ink);
  }
  .contacts li { display: flex; align-items: center; gap: 10px; }
  .contacts svg { width: 14px; height: 14px; flex: none; }
</style>
</head>
<body>
<main class="stage">

  <section class="card card-back" aria-label="Card back">
    <div class="pattern" role="img" aria-label="Repeating tonal brand pattern across the grey background"></div>
    <div class="brand"><span class="brand-square"></span>Hillcrest Building Group</div>
    <p class="services">
      Design-Build Services<span class="dot"></span>Project Management<span class="dot"></span>Kitchen &amp; Bath Remodeling<br>
      Specialty Services: Cabinets<span class="dot"></span>Carpentry<span class="dot"></span>Flooring<span class="dot"></span>Tile - Stone
    </p>
  </section>

  <section class="card card-front" aria-label="Card front">
    <div class="brand"><span class="brand-square"></span>Hillcrest Building Group</div>

    <div class="holder">
      <div>
        <h1 class="holder-name">Daniel <span class="surname">Reyes</span></h1>
        <p class="holder-title">CA Contractors License - 100234</p>
      </div>
      <span class="holder-bar"></span>
    </div>

    <p class="address">482 Meadowbrook Ave Suite<br>210-118 Oakridge, CA 90000</p>

    <ul class="contacts">
      <li>
        <svg viewBox="0 0 16 16"><path d="M3 1.5l2.5 0 1 3.5-1.6 1.2a8 8 0 0 0 4.9 4.9L11 9.5l3.5 1v2.5c0 1-1 1.5-2 1.5C6.5 14.5 1.5 9.5 1.5 3.5c0-1 .5-2 1.5-2z" fill="var(--brand-blue)"/></svg>
        555.201.4470
      </li>
      <li>
        <svg viewBox="0 0 16 16"><rect x="4" y="1" width="8" height="14" rx="1.5" fill="none" stroke="var(--brand-blue)" stroke-width="1.5"/></svg>
        555.318.9026
      </li>
      <li>
        <svg viewBox="0 0 16 16"><circle cx="8" cy="8" r="6.5" fill="none" stroke="var(--brand-blue)" stroke-width="1.5"/><path d="M1.5 8h13M8 1.5c-3 3.5-3 9.5 0 13M8 1.5c3 3.5 3 9.5 0 13" fill="none" stroke="var(--brand-blue)" stroke-width="1.2"/></svg>
        www.hillcrestbuilding.com
      </li>
      <li>
        <svg viewBox="0 0 16 16"><rect x="1.5" y="3.5" width="13" height="9" rx="1" fill="none" stroke="var(--brand-blue)" stroke-width="1.5"/><path d="M1.5 4l6.5 5 6.5-5" fill="none" stroke="var(--brand-blue)" stroke-width="1.5"/></svg>
        daniel@hillcrestbuilding.com
      </li>
    </ul>
  </section>

</main>
</body>
</html>
```